Business Card Design Project

New Business Card design for Travorel Technology Ltd using new Logo and new Tagline for staffing company.

About us from our website - www.travorel-example.net:

TraVorel is a leading and recognized Electronic Entertainment, Workforce Augmentation, and Project Management solutions provider with clients in Electronic Entertainment, Legal, Technology, Government and other verticals that range in size from start up organizations to Zentora 300 companies. TraVorel is certified as an 8(a) minority and woman owned enterprise, established in 1998.

Target Market(s)

Companies in Electronic Entertainment, Legal, Government and Technology

Industry/Entity Type

Business

Requirements
Must have
• Must include in small letters the following information on back:

Established in 1998
8(a)(w)(e), Cage #7KQW4, DUNS #412306957

Front should have the following:
Dale Merrow
Vice President
5870 Brookhollow Court
Lindenvale, QX 908172
555-318-2046 X 100
555-742-9813 Fax
555-318-2046 Toll Free
name@travorel-example.net

Our Tagline: Connect • Collaborate • Achieve

```html
<!DOCTYPE html>
<html lang="en">
<head>
<meta charset="utf-8">
<title>TraVorel Business Card</title>
<link rel="stylesheet" href="https://fonts.googleapis.com/css2?family=Arimo:wght@400;500;700&family=Tinos:wght@700&display=swap">
<style>
  :root {
    --page: #ffffff;
    --brand-blue: #1a66ff;
    --card-black: #030405;
    --ink-light: #ffffff;
  }
  html, body {
    margin: 0;
    padding: 0;
    overflow: hidden;
  }
  .canvas {
    position: relative;
    width: 869px;
    height: 1200px;
    background: var(--page);
    overflow: hidden;
  }
  .card {
    position: absolute;
    left: 237px;
    width: 355px;
    overflow: hidden;
  }
  .card-front {
    top: 286px;
    height: 197px;
    background: var(--card-black);
  }
  .card-back {
    top: 514px;
    height: 198px;
    background: var(--card-black);
  }
  .front-panel {
    position: absolute;
    inset: 0;
  }
  .holder-name {
    position: absolute;
    left: 15px;
    top: 25px;
    margin: 0;
    font: 500 25px/1 "Arimo", Arial, sans-serif;
    color: var(--ink-light);
    letter-spacing: 0.3px;
  }
  .holder-title {
    position: absolute;
    left: 41px;
    top: 60px;
    margin: 0;
    font: 500 12px/1 "Arimo", Arial, sans-serif;
    color: var(--ink-light);
  }
  .contact-list {
    position: absolute;
    left: 9px;
    top: 134px;
    margin: 0;
    padding: 0;
    list-style: none;
    font: 700 8.3px/10.3px "Tinos", "Times New Roman", serif;
    letter-spacing: 0.15px;
    color: var(--ink-light);
  }
  .wordmark {
    position: absolute;
    display: flex;
    align-items: center;
    color: var(--ink-light);
    font-family: "Arimo", Arial, sans-serif;
    font-weight: 700;
    white-space: nowrap;
  }
  .wordmark .dot {
    border-radius: 50%;
    background: var(--brand-blue);
    flex: none;
  }
  .wordmark-front {
    left: 243px;
    top: 36px;
    font-size: 21px;
    gap: 6px;
  }
  .wordmark-front .dot {
    width: 10px;
    height: 10px;
  }
  .wordmark-back {
    left: 0;
    right: 0;
    top: 78px;
    justify-content: center;
    font-size: 37px;
    gap: 10px;
  }
  .wordmark-back .dot {
    width: 16px;
    height: 16px;
  }
  .legal {
    position: absolute;
    left: 6px;
    top: 177px;
    margin: 0;
    font: 400 5.6px/10.5px "Arimo", Arial, sans-serif;
    letter-spacing: 0.3px;
    color: var(--ink-light);
  }
</style>
</head>
<body>
<main class="canvas">
  <section class="card card-front" aria-label="Card front">
    <svg class="front-panel" width="355" height="197" viewBox="0 0 355 197" aria-hidden="true">
      <polygon points="0,0 180,0 355,197 0,197" fill="var(--brand-blue)"/>
    </svg>
    <h1 class="holder-name">Dale Merrow</h1>
    <p class="holder-title">Vice President</p>
    <ul class="contact-list">
      <li>Brookhollow Court Lindenvale, QX 908172 5870</li>
      <li>X 100 555-318-2046</li>
      <li>Fax 555-742-9813</li>
      <li>Toll Free 555-318-2046</li>
      <li>name@travorel-example.net</li>
    </ul>
    <div class="wordmark wordmark-front"><span class="dot"></span>TraVorel</div>
  </section>

  <section class="card card-back" aria-label="Card back">
    <div class="wordmark wordmark-back"><span class="dot"></span>TraVorel</div>
    <p class="legal">Established in 1998<br>8(a)(w)(e), Cage #7KQW4, DUNS #412306957</p>
  </section>
</main>
</body>
</html>
```